Business Card Design

Freelance writer, coach, teacher and researcher specialising in improving mathematics teaching and learning in primary schools. I write books and articles for teachers, speak extensively at conferences in UK and aboard. Would like something with a cube in the design. Clean, modern - logo suitable for use on a website. Should NOT look 'childish' (no comic sans or chalkboard type fonts)

Full details to go on card:

Professor Dale Voronin
Building Early Numeracy

info@dalevoronin.net
#dalevoronin26
www.dalevoronin.net
+44 7823 608 142

Industry/Entity Type

Teacher

Contact Information for Business Card

Professor Dale Voronin
Building Early Numeracy

```html
<!DOCTYPE html>
<html lang="en">
<head>
<meta charset="utf-8">
<title>Dale Voronin – Business Card</title>
<link rel="stylesheet" href="https://fonts.googleapis.com/css2?family=Open+Sans:wght@400;600&display=swap">
<style>
  :root {
    --backdrop: #d6d7d8;
    --card: #ffffff;
    --blue-deep: #0a86d2;
    --blue-mid: #2aa7e6;
    --blue-pale: #d3ebf7;
    --ink: #161616;
  }
  html, body {
    margin: 0;
    width: 1200px;
    height: 900px;
    overflow: hidden;
    background: var(--backdrop);
  }
  .canvas {
    width: 1200px;
    height: 900px;
    display: flex;
    align-items: center;
    justify-content: center;
  }
  .card {
    position: relative;
    width: 840px;
    height: 500px;
    background: var(--card);
    overflow: hidden;
    box-shadow: 0 10px 30px rgba(0, 0, 0, 0.18);
  }
  .card__accent {
    position: absolute;
    top: 0;
    right: 0;
    width: 270px;
    height: 100%;
    background: linear-gradient(215deg, var(--blue-pale) 0%, var(--blue-mid) 55%, var(--blue-deep) 100%);
  }
  .brand {
    position: absolute;
    left: 60px;
    top: 56px;
    display: flex;
    align-items: center;
    gap: 14px;
    font-family: "Open Sans", sans-serif;
    font-weight: 600;
    font-size: 26px;
    color: var(--blue-deep);
  }
  .brand__square {
    width: 46px;
    height: 46px;
    background: var(--blue-mid);
  }
  .details {
    position: absolute;
    left: 60px;
    top: 160px;
    font-family: "Open Sans", sans-serif;
    color: var(--ink);
  }
  .details p {
    margin: 0;
    line-height: 1.35;
  }
  .details__name,
  .details__tagline {
    font-size: 24px;
  }
  .details__tagline {
    margin-bottom: 12px !important;
  }
  .details__line {
    font-size: 26px;
    margin-bottom: 4px !important;
  }
  .details__web {
    font-size: 26px;
    margin-top: 12px !important;
  }
</style>
</head>
<body>
<main class="canvas">
  <section class="card">
    <div class="card__accent" role="img" aria-label="Blue gradient swoosh decoration"></div>

    <div class="brand">
      <span class="brand__square"></span>
      <span class="brand__name">Dale Voronin</span>
    </div>

    <div class="details">
      <p class="details__name">Professor Dale Voronin</p>
      <p class="details__tagline">Building Early Numeracy</p>
      <p class="details__line">Contact : +44 7823 608 142</p>
      <p class="details__line">E-mail : info@dalevoronin.net</p>
      <p class="details__line">#dalevoronin26</p>
      <p class="details__web">www.dalevoronin.net</p>
    </div>
  </section>
</main>
</body>
</html>
```